CBD Boutique Business Card Needed

We are in need of a business card to reflect the direction of our latest products. We are a fully organic company in which our store and products are very heavy in wood and "natural" components. We decided to bring color into one of our brands and immediately knew this is where we needed to go.

We are NOT a cash grab CBD company. We could have done this wrong, slapped a label on a shit product and left it like that. I am passionate about sharing my experience with other veterans and opening a store and making it a comfortable place for others to come and see if they can have the same experience.

Target Market(s)

We are a dual market company. We do have a beauty line that will cover the costs of the majority of our business. But we also heavily cater to veterans and first responders. I am a veteran and this is how I found out about CBD. So the marketing needs to bring in our higher end beauty clientele but also be able to not put off our customers that readily need this.

Contact Information for Business Card

What we are looking for is a light, professional, boutique design that is is neither quite feminine or masculine. Attached is a picture of a store in Portland that we asked our store designer to get her inspiration from. But all natural wood and black outlines are what is mostly in there.

Attached are the following files:

Logo: An AI file with how we have our logo. I do not understand AI and have no idea why the letters are individual. The font is Adam. OLU is the logo and Tonics of Vigor is our tagline.

KM Vantage (front and back) cards I did originally found at a trade show that I absolutely loved...while it is mostly there and I would still be happy with them but it is me pretending to be you. I understand I am not and there is probably a lot wrong that all of you would see instantly and this is why I am here.

Dropper Bottle: This is our final product mock up

Water Color: I am semi flexible here. This water color is slightly different on every level of our brand. The color itself can change...we are not stuck on THIS particular one. If you happen to make a new one that is similar in style and we use it...then I will happily commission you to change the rest on our next product run. I am pretty sure you can use this statement as evidence later . =) .

But seriously, we heavily believe in pay it forward and will work with anyone here that may have a vision bigger than ours. The winner of this contest will get preferential consideration on our marketing materials (need letterhead etc. next, as well as a brochure, and website) so three more projects coming down the pipeline.

Information to use for your mockup is contained on the card images I have included. I would prefer CBD for wellness CBD for life to be more prominent. No where else on the card do we have CBD mentioned.

Font styles to use
Sans Serif

Colors

Designer to choose colors to be used in the design.

Requirements
Must have
• Double Sided
• Front: OLU logo on front of card will be raised embossed. Background is watercolor. One has been provided. Others are up for consideration. If the rest of your design is incredible and I don't like your watercolor I will just ask to swap it.
• Back: Standard information. Not stuck on anything here. I LOVE clean minimal designs. The bleed on the card I provided is a luxury...
• Font for title and OLU is Adam. Everything else I prefer san serif or as clean as possible.
Nice to have
• I Need to incorporate Naturally Nurturing somewhere on the card. Bold but not intrusive.

```html
<!DOCTYPE html>
<html lang="en">
<head>
<meta charset="utf-8">
<title>OLU – Tonics of Vigor business card</title>
<link rel="stylesheet" href="https://fonts.googleapis.com/css2?family=Lato:wght@300;400&family=Montserrat:wght@300;400;800&display=swap">
<style>
  :root {
    --backdrop-center: #2e2e2f;
    --backdrop-edge: #000000;
    --paper: #ffffff;
    --teal: #2a8f8c;
    --teal-bright: #22adb6;
    --amber: #e5902f;
    --rust: #cf6a24;
    --ink: #1a1a1a;
    --ink-soft: #2a2a2a;
  }
  * { margin: 0; padding: 0; box-sizing: border-box; }
  html, body { width: 1200px; height: 849px; overflow: hidden; }
  body {
    position: relative;
    background: radial-gradient(circle at 50% 50%, var(--backdrop-center) 0%, #111 40%, var(--backdrop-edge) 75%);
    font-family: "Lato", sans-serif;
  }

  .card { position: absolute; background: var(--paper); overflow: hidden; }

  /* Front */
  .card-front { left: 118px; top: 99px; width: 533px; height: 311px; }
  .watercolor {
    position: absolute; inset: 0;
    background: linear-gradient(100deg, var(--amber) 0%, var(--rust) 40%, var(--teal) 62%, var(--teal-bright) 100%);
  }
  .frame-outer {
    position: absolute; left: 23px; top: 21px; width: 494px; height: 265px;
    border: 2px solid var(--paper);
  }
  .frame-inner {
    position: absolute; left: 108px; top: 92px; width: 324px; height: 126px;
    border: 1.5px solid var(--paper);
  }
  .logo-panel {
    position: absolute; left: 117px; top: 98px; width: 307px; height: 113px;
    background: var(--paper);
    color: var(--teal);
    text-align: center;
  }
  .logo-panel .brand-name {
    position: absolute; left: 0; right: 0; top: 10px;
    font-family: "Lato", sans-serif; font-weight: 300;
    font-size: 80px; line-height: 80px; letter-spacing: 6px; padding-left: 6px;
  }
  .logo-panel .tagline {
    position: absolute; left: 0; right: 0; top: 85px;
    font-family: "Lato", sans-serif; font-weight: 400;
    font-size: 19px; line-height: 22px; letter-spacing: 0.5px;
  }
  .website {
    position: absolute; left: 0; right: 0; top: 221px; text-align: center;
    color: var(--paper); font-family: "Montserrat", sans-serif; font-weight: 400;
    font-size: 12px; line-height: 14px; letter-spacing: 10px; padding-left: 10px;
  }

  /* Back */
  .card-back { left: 520px; top: 472px; width: 539px; height: 311px; text-align: center; color: var(--ink); }
  .back-logo .brand-name {
    position: absolute; left: 0; right: 0; top: 57px;
    font-family: "Lato", sans-serif; font-weight: 400;
    font-size: 50px; line-height: 50px; letter-spacing: 3px; padding-left: 3px;
  }
  .back-logo .tagline {
    position: absolute; left: 0; right: 0; top: 104px;
    font-size: 11px; line-height: 13px; letter-spacing: 0.3px;
  }
  .divider {
    position: absolute; left: 97px; top: 134px; width: 345px; height: 2px; background: var(--teal);
  }
  .person-name {
    position: absolute; left: 0; right: 0; top: 144px;
    font-family: "Montserrat", sans-serif; font-weight: 300; font-size: 20px; line-height: 24px;
  }
  .person-name strong { font-weight: 800; }
  .person-role {
    position: absolute; left: 0; right: 0; top: 168px;
    font-family: "Montserrat", sans-serif; font-size: 10px; line-height: 12px; letter-spacing: 6px; padding-left: 6px;
  }
  .contact { position: absolute; left: 0; right: 0; font-weight: 400; color: var(--ink-soft); }
  .contact.phone { top: 195px; font-size: 15px; line-height: 18px; letter-spacing: 4px; padding-left: 4px; }
  .contact.email { top: 216px; font-size: 13.5px; line-height: 17px; letter-spacing: 1.5px; }
  .contact.address { top: 237px; font-size: 14px; line-height: 17px; letter-spacing: 1.5px; }
</style>
</head>
<body>
  <section class="card card-front">
    <div class="watercolor" role="img" aria-label="Watercolor wash in amber, rust and teal tones"></div>
    <div class="frame-outer"></div>
    <div class="frame-inner"></div>
    <div class="logo-panel">
      <div class="brand-name">OLU</div>
      <div class="tagline">TONICS OF VIGOR</div>
    </div>
    <div class="website">www.olu.vigor.com</div>
  </section>

  <section class="card card-back">
    <div class="back-logo">
      <div class="brand-name">OLU</div>
      <div class="tagline">TONICS OF VIGOR</div>
    </div>
    <div class="divider"></div>
    <div class="person-name">Dana <strong>Whitlock</strong></div>
    <div class="person-role">Owner / CEO</div>
    <div class="contact phone">555.014.2290</div>
    <div class="contact email">hello@olu.vigor.com</div>
    <div class="contact address">4120 W Marlow Rd<br>Fairview, AZ 85000 Suite 100</div>
  </section>
</body>
</html>
```